Terravista NQ PPT template - non-profit company - minerals, energy, water, geothermal resources

Terravista NQ requires two (Letter-sized and 16:9)simple, flexible and clean PowerPoint templates that can be used for corporate and research project presentations and meeting materials

Each layout should have correct colours, fonts and size as a default (focus area colours for headings; secondary colours for body text). Each slide should have the Terravista NQ logo. Slide number should be automatically generated, with no slide number on title slide.

Target Market(s)

Varied, but almost always professional: Government; Community leaders; Mineral/Energy industries; and Academic researchers.

Font styles to use
Serif
Sans Serif
Other font styles liked:
• Calibri, or whatever in style guide

Requirements
Must have
• Two version that we can use – both need to match:
- 16:9 slide size for on-screen presentations; and
- Letter (8.5 x 11 inch) for meeting materials that are printed.

Must use colours in logo as listed in the style guide
Nice to have
• Consistency
Should not have
• Should not be black and white - needs colour

```html
<!DOCTYPE html>
<html lang="en">
<head>
<meta charset="utf-8">
<title>Terravista NQ – Master Slide Set</title>
<link href="https://fonts.googleapis.com/css2?family=Montserrat:wght@400;500;600;700;800&family=Open+Sans:wght@400;600&display=swap" rel="stylesheet">
<style>
  :root{
    --canvas:#e4e4e4;
    --orange:#e2783a;
    --orange-dark:#cf6526;
    --green:#0aad4e;
    --green-dark:#2f8c3c;
    --blue:#21a5c6;
    --blue-dark:#237fa8;
    --slate:#4a5866;
    --slate-light:#6b7784;
    --ink:#2b2b2b;
    --body:#6d6d6d;
    --panel-grey:#ebebeb;
    --white:#ffffff;
  }
  *{margin:0;padding:0;box-sizing:border-box}
  html,body{width:1200px;height:2827px;overflow:hidden;background:var(--canvas)}
  body{position:relative;font-family:'Montserrat',sans-serif;color:var(--slate)}
  .slide{position:absolute;width:566px;height:318px;background:var(--white);overflow:hidden;box-shadow:0 3px 6px rgba(0,0,0,.22)}
  .col-l{left:22px}.col-r{left:606px}
  .r1{top:25px}.r2{top:374px}.r3{top:724px}.r4{top:1073px}.r5{top:1422px}.r6{top:1771px}.r7{top:2120px}.r8{top:2469px}
  .abs{position:absolute}
  .photo{position:absolute}
  .brand{position:absolute;font-family:'Montserrat',sans-serif;font-weight:600;color:var(--slate);white-space:nowrap}
  .brand-sm{font-size:7px;top:10px;right:8px}
  .brand-corner{font-size:7px;right:8px;bottom:8px}
  .slide-no{position:absolute;right:0;bottom:0;width:10px;height:10px;font-size:5px;color:#fff;text-align:center;line-height:10px}
  .edge-r{position:absolute;right:0;top:0;width:2px;height:100%}
  .page-title{position:absolute;left:16px;top:12px;font-weight:700;font-size:17px;letter-spacing:.3px}
  .page-title::before{content:"";position:absolute;left:-16px;top:0;width:3px;height:100%;background:currentColor}
  .lorem{font-family:'Open Sans',sans-serif;font-size:6.2px;line-height:1.9;color:var(--body);text-align:justify}
  .subhead{font-weight:700;font-size:8.5px;color:var(--ink)}
  .btn{position:absolute;font-size:6px;font-weight:700;letter-spacing:1.5px;color:#fff;padding:3px 6px;box-shadow:2px 2px 0 rgba(0,0,0,.15)}
  .feature-art{position:absolute;left:14px;top:88px;width:240px;height:170px;border-radius:4px}
  .section-title{position:absolute;left:21px;top:201px;font-size:27px;font-weight:800;color:#fff;letter-spacing:.5px}
  .section-rule{position:absolute;left:10px;top:205px;width:2px;height:70px;background:#fff}
  .section-tag{position:absolute;left:21px;font-size:5.5px;font-weight:700;color:#fff}
  .section-text{position:absolute;left:21px;width:240px;font-size:6px;font-weight:600;color:#fff;line-height:1.3}
  .cover-contact{position:absolute;left:0;right:0;bottom:5px;display:flex;justify-content:center;gap:10px;font-size:6.3px;color:var(--slate)}
  .bullet-text{position:absolute;width:120px;font-size:6.8px;line-height:1.4;color:var(--slate-light)}
</style>
</head>
<body>

<!-- 1 Cover -->
<section class="slide col-l r1">
  <div class="photo" role="img" aria-label="Pale grey aerial view of an open-pit mine" style="inset:0;background:linear-gradient(135deg,#d9dadb,#eeeeee 45%,#d2d3d4 80%,#e6e6e6)"></div>
  <div class="abs" style="top:6px;width:100%;text-align:center;font-size:6.5px;letter-spacing:3px;font-weight:600">WWW.TERRAVISTANQ.ORG</div>
  <div class="brand" style="left:0;right:0;text-align:center;top:164px;font-size:28px">Terravista NQ</div>
  <div class="cover-contact"><span>☏ (555) 014 2290</span><span>|</span><span>www.terravistanq.org</span><span>|</span><span>✉ hello@terravistanq.org</span><span>|</span><span>Suite 410 - 88 Harbour Row, Northgate, NQ</span></div>
</section>

<!-- 2 Master title -->
<section class="slide col-r r1">
  <div class="photo" role="img" aria-label="Dark rocky mountain surface" style="left:0;right:0;top:66px;bottom:0;background:linear-gradient(160deg,#3a3a3a,#1e1e1e 55%,#2c2c2c)"></div>
  <div class="brand" style="left:0;right:0;text-align:center;top:32px;font-size:16px">Terravista NQ</div>
  <div class="abs" style="top:139px;width:100%;text-align:center;color:#ddd;font-size:6.5px;letter-spacing:2.5px">www.terravistanq.org</div>
  <div class="abs" style="top:172px;width:100%;text-align:center;color:#fff;font-size:29px;font-weight:700">Master Slide Presentation</div>
  <div class="abs" style="top:211px;width:100%;text-align:center;color:#ddd;font-size:7px;letter-spacing:3px">subtitle goes here</div>
  <div class="abs" style="top:250px;width:100%;text-align:center;color:#fff;font-size:7.5px;font-weight:700">2020</div>
  <svg class="abs" style="left:261px;top:282px" width="44" height="12" viewBox="0 0 44 12"><g fill="none" stroke="#fff" stroke-width="1"><circle cx="6" cy="6" r="5"/><circle cx="22" cy="6" r="5"/><circle cx="38" cy="6" r="5"/></g></svg>
</section>

<!-- 3 Presentation title -->
<section class="slide col-l r2">
  <div class="brand" style="left:36px;top:150px;font-size:27px">Terravista NQ</div>
  <div class="abs" style="left:279px;top:12px;width:2px;height:290px;background:var(--slate)"></div>
  <div class="abs" style="right:23px;top:38px;text-align:right;font-size:25px;font-weight:700;line-height:1.25">Presentation<br>Title Name</div>
  <div class="abs" style="right:23px;top:105px;font-size:7px;letter-spacing:1.5px;color:var(--slate)">subtitle goes here</div>
  <div class="abs" style="right:23px;top:268px;font-size:7px;font-weight:600;color:var(--orange)">PRESENTER NAME</div>
  <div class="abs" style="right:23px;top:282px;font-size:7px;font-weight:600">DATE</div>
</section>

<!-- 4 Minerals section -->
<section class="slide col-r r2" style="background:var(--orange)">
  <svg class="abs" style="inset:0" width="566" height="318" viewBox="0 0 566 318">
    <polygon points="0,0 283,0 0,175" fill="var(--orange-dark)"/>
    <polygon points="283,0 566,0 566,185 349,318 160,318 409,163" fill="#8a8a86" role="img" aria-label="Aerial photograph of a mine site"/>
    <polygon points="349,318 566,185 566,318" fill="#fff"/>
  </svg>
  <div class="section-rule"></div>
  <div class="section-title">MINERALS</div>
  <div class="section-text" style="top:238px">Responsible mineral exploration projects and mining operations in the region continue to benefit communities, provide thousands of jobs and contribute billions of dollars in economic activity.</div>
  <div class="brand brand-corner">Terravista NQ</div>
</section>

<!-- 5 Minerals content -->
<section class="slide col-l r3">
  <div class="page-title" style="color:var(--orange)">MINERALS</div>
  <div class="brand brand-sm">Terravista NQ</div>
  <div class="feature-art" role="img" aria-label="Illustration of a magnifying glass over a pickaxe" style="background:linear-gradient(135deg,#f6e3d6,#ececec 60%,#f3f3f3)"></div>
  <div class="subhead abs" style="left:283px;top:87px">ADD YOUR SUBTITLE HERE</div>
  <p class="lorem abs" style="left:283px;top:108px;width:240px">Lorem ipsum dolor sit amet, consectetuer adipiscing elit, sed diam nonummy nibh euismod tincidunt ut laoreet dolore magna aliquam erat volutpat. Ut wisi enim ad minim veniam, quis nostrud exerci tation ullamcorper suscipit lobortis nisl ut aliquip ex ea commodo consequat. Duis autem vel eum iriure dolor in hendrerit in vulputate velit esse molestie consequat, vel illum dolore eu feugiat nulla facilisis at vero eros et accumsan et iusto odio dignissim qui blandit praesent luptatum zzril delenit augue duis dolore te feugait nulla facilisi.</p>
  <div class="btn" style="left:280px;top:255px;background:var(--orange)">LEARN MORE</div>
  <div class="edge-r" style="background:var(--orange);top:250px;height:68px"></div>
  <div class="slide-no" style="background:var(--orange)">5</div>
</section>

<!-- 6 Energy section -->
<section class="slide col-r r3" style="background:var(--green)">
  <svg class="abs" style="inset:0" width="566" height="318" viewBox="0 0 566 318">
    <polygon points="0,0 283,0 0,175" fill="var(--green-dark)"/>
    <polygon points="283,0 566,0 566,185 349,318 160,318 409,163" fill="#6f8c8a" role="img" aria-label="Snow-capped mountains above a forested valley"/>
    <polygon points="349,318 566,185 566,318" fill="#fff"/>
  </svg>
  <div class="section-rule"></div>
  <div class="section-title" style="top:197px">ENERGY</div>
  <div class="section-tag" style="top:232px">OIL &amp; GAS | GEOTHERMAL</div>
  <div class="section-text" style="top:248px">Geothermal may play a significant role as we transition to alternative sources for electricity and heat.</div>
  <div class="brand brand-corner">Terravista NQ</div>
</section>

<!-- 7 Energy content -->
<section class="slide col-l r4">
  <div class="page-title" style="color:var(--green)">ENERGY</div>
  <div class="brand brand-sm">Terravista NQ</div>
  <div class="feature-art" role="img" aria-label="Illustration of a magnifying glass over a light bulb" style="background:linear-gradient(135deg,#d6f0df,#ececec 60%,#f3f3f3)"></div>
  <div class="subhead abs" style="left:283px;top:87px">ADD YOUR SUBTITLE HERE</div>
  <p class="lorem abs" style="left:283px;top:108px;width:240px">Lorem ipsum dolor sit amet, consectetuer adipiscing elit, sed diam nonummy nibh euismod tincidunt ut laoreet dolore magna aliquam erat volutpat. Ut wisi enim ad minim veniam, quis nostrud exerci tation ullamcorper suscipit lobortis nisl ut aliquip ex ea commodo consequat. Duis autem vel eum iriure dolor in hendrerit in vulputate velit esse molestie consequat, vel illum dolore eu feugiat nulla facilisis at vero eros et accumsan et iusto odio dignissim qui blandit praesent luptatum zzril delenit augue duis dolore te feugait nulla facilisi.</p>
  <div class="btn" style="left:280px;top:255px;background:var(--green)">LEARN MORE</div>
  <div class="edge-r" style="background:var(--green);top:250px;height:68px"></div>
  <div class="slide-no" style="background:var(--green)">7</div>
</section>

<!-- 8 Water section -->
<section class="slide col-r r4" style="background:var(--blue)">
  <svg class="abs" style="inset:0" width="566" height="318" viewBox="0 0 566 318">
    <polygon points="0,0 283,0 0,175" fill="var(--blue-dark)"/>
    <polygon points="283,0 566,0 566,185 349,318 160,318 409,163" fill="#8f8fb6" role="img" aria-label="City skyline reflected in a lake at dusk"/>
    <polygon points="349,318 566,185 566,318" fill="#fff"/>
  </svg>
  <div class="section-rule"></div>
  <div class="section-title">WATER</div>
  <div class="section-text" style="top:244px">Water research is principally related to energy and mineral development in the region.</div>
  <div class="brand brand-corner">Terravista NQ</div>
</section>

<!-- 9 Water content -->
<section class="slide col-l r5">
  <div class="page-title" style="color:var(--blue)">WATER</div>
  <div class="brand brand-sm">Terravista NQ</div>
  <div class="feature-art" role="img" aria-label="Illustration of a magnifying glass over a water drop" style="background:linear-gradient(135deg,#d4edf4,#ececec 60%,#f3f3f3)"></div>
  <div class="subhead abs" style="left:283px;top:87px">ADD YOUR SUBTITLE HERE</div>
  <p class="lorem abs" style="left:283px;top:108px;width:240px">Lorem ipsum dolor sit amet, consectetuer adipiscing elit, sed diam nonummy nibh euismod tincidunt ut laoreet dolore magna aliquam erat volutpat. Ut wisi enim ad minim veniam, quis nostrud exerci tation ullamcorper suscipit lobortis nisl ut aliquip ex ea commodo consequat. Duis autem vel eum iriure dolor in hendrerit in vulputate velit esse molestie consequat, vel illum dolore eu feugiat nulla facilisis at vero eros et accumsan et iusto odio dignissim qui blandit praesent luptatum zzril delenit augue duis dolore te feugait nulla facilisi.</p>
  <div class="btn" style="left:280px;top:255px;background:var(--blue)">LEARN MORE</div>
  <div class="edge-r" style="background:var(--blue);top:250px;height:68px"></div>
  <div class="slide-no" style="background:var(--blue)">9</div>
</section>

<!-- 10 Image with text layout 1 -->
<section class="slide col-r r5">
  <div class="photo" role="img" aria-label="Close-up of golden mineral crystals" style="left:0;top:0;width:199px;height:155px;background:linear-gradient(135deg,#7a5a30,#c49a55 50%,#5e4a35)"></div>
  <div class="photo" role="img" aria-label="Close-up of pale quartz crystals" style="left:0;top:155px;width:199px;height:163px;background:linear-gradient(135deg,#c9c6bd,#8d8a82 55%,#d8d5cc)"></div>
  <div class="abs" style="left:0;top:0;width:60px;height:155px;background:var(--orange);opacity:.92"></div>
  <div class="abs" style="left:0;top:155px;width:60px;height:163px;background:var(--slate);opacity:.92"></div>
  <div class="abs" style="left:26px;top:120px;transform:rotate(-90deg);transform-origin:left top;color:#fff;font-size:7.5px;white-space:nowrap">Lorem ipsum dolor</div>
  <div class="abs" style="left:26px;top:285px;transform:rotate(-90deg);transform-origin:left top;color:#fff;font-size:7.5px;white-space:nowrap">Lorem ipsum dolor</div>
  <div class="abs" style="left:100px;top:24px;width:373px;height:32px;background:#fff;box-shadow:2px 2px 4px rgba(0,0,0,.2);text-align:center;line-height:32px;font-size:16.5px;font-weight:700">IMAGE WITH TEXT LAYOUT 1</div>
  <div class="brand brand-sm">Terravista NQ</div>
  <div class="abs" style="left:228px;top:80px;width:1.5px;height:80px;background:var(--orange)"></div>
  <p class="lorem abs" style="left:241px;top:78px;width:290px">Lorem ipsum dolor sit amet, consectetuer adipiscing elit, sed diam nonummy nibh euismod tincidunt ut laoreet dolore magna aliquam erat volutpat. Ut wisi enim ad minim veniam, quis nostrud exerci tation ullamcorper suscipit lobortis nisl ut aliquip ex ea commodo consequat. Duis autem vel eum iriure dolor in hendrerit in vulputate velit esse molestie consequat, vel illum dolore eu feugiat nulla facilisis at vero eros et accumsan et.</p>
  <div class="abs" style="left:228px;top:198px;width:1.5px;height:80px;background:var(--slate)"></div>
  <p class="lorem abs" style="left:241px;top:198px;width:290px">Lorem ipsum dolor sit amet, consectetuer adipiscing elit, sed diam nonummy nibh euismod tincidunt ut laoreet dolore magna aliquam erat volutpat. Ut wisi enim ad minim veniam, quis nostrud exerci tation ullamcorper suscipit lobortis nisl ut aliquip ex ea commodo consequat. Duis autem vel eum iriure dolor in hendrerit in vulputate velit esse molestie consequat, vel illum dolore eu feugiat nulla facilisis at vero eros et accumsan et.</p>
  <div class="edge-r" style="background:var(--orange)"></div>
  <div class="slide-no" style="background:var(--orange)">10</div>
</section>

<!-- 11 Image with text layout 2 -->
<section class="slide col-l r6">
  <div class="page-title" style="color:var(--slate);font-size:16.5px">IMAGE WITH TEXT LAYOUT 2</div>
  <div class="abs" style="left:0;top:125px;width:310px;height:193px;background:var(--panel-grey)"></div>
  <div class="abs" style="left:310px;top:0;width:188px;height:318px;background:var(--green)"></div>
  <div class="photo" role="img" aria-label="Researchers reviewing a large map together" style="left:352px;top:52px;width:193px;height:128px;background:linear-gradient(135deg,#6d6a66,#b9b3a8 50%,#4f5358);box-shadow:2px 2px 4px rgba(0,0,0,.3)"></div>
  <div class="brand brand-sm">Terravista NQ</div>
  <svg class="abs" style="left:30px;top:62px" width="44" height="52" viewBox="0 0 44 52"><g fill="none" stroke="var(--green)" stroke-width="1.6" stroke-linecap="round"><circle cx="22" cy="22" r="11"/><path d="M17 33 v8 h10 v-8"/><line x1="18" y1="45" x2="26" y2="45"/><line x1="22" y1="4" x2="22" y2="1"/><line x1="7" y1="10" x2="5" y2="8"/><line x1="37" y1="10" x2="39" y2="8"/><line x1="4" y1="23" x2="1" y2="23"/><line x1="40" y1="23" x2="43" y2="23"/></g></svg>
  <div class="abs" style="right:280px;top:105px;font-size:9px;font-weight:700;color:var(--green)">Add your subtitle here</div>
  <p class="lorem abs" style="left:36px;top:142px;width:250px;font-size:6.6px">Lorem ipsum dolor sit amet, consectetuer adipiscing elit, sed diam nonummy nibh euismod tincidunt ut laoreet dolore magna aliquam erat volutpat. Ut wisi enim ad minim veniam, quis nostrud exerci tation ullamcorper suscipit lobortis nisl ut aliquip ex ea commodo consequat. Duis autem vel eum iriure dolor in hendrerit in vulputate velit esse molestie consequat, vel illum dolore eu feugiat nulla facilisis at vero eros et accumsan et iusto odio dignissim qui blandit praesent luptatum zzril delenit augue duis dolore te feugait nulla facilisi.</p>
  <p class="lorem abs" style="left:332px;top:203px;width:148px;color:#fff;font-size:6.6px">Lorem ipsum dolor sit amet, consectetuer adipiscing elit, sed diam nonummy nibh euismod tincidunt ut laoreet dolore magna aliquam erat volutpat. Ut wisi enim ad minim veniam,</p>
  <div class="slide-no" style="background:var(--green)">11</div>
</section>

<!-- 12 Image with text layout 3 -->
<section class="slide col-r r6">
  <div class="page-title" style="color:var(--slate);font-size:16.5px">IMAGE WITH TEXT LAYOUT 3</div>
  <div class="brand brand-sm">Terravista NQ</div>
  <div class="photo" role="img" aria-label="Helicopter parked on a gravel clearing beside forest" style="left:16px;top:57px;width:222px;height:127px;background:linear-gradient(180deg,#6e9bc8 0%,#3e6a3e 45%,#a99c84 75%,#bdb19a)"></div>
  <div class="abs" style="left:267px;top:58px;width:1.5px;height:120px;background:var(--orange)"></div>
  <div class="abs" style="left:278px;top:55px;font-size:9px;font-weight:700;color:var(--blue)">Add your subtitle here</div>
  <p class="lorem abs" style="left:278px;top:68px;width:270px">Lorem ipsum dolor sit amet, consectetuer adipiscing elit, sed diam nonummy nibh euismod tincidunt ut laoreet dolore magna aliquam erat volutpat. Ut wisi enim ad minim veniam, quis nostrud exerci tation ullamcorper suscipit lobortis nisl ut aliquip ex ea commodo consequat. Duis autem vel eum iriure dolor in hendrerit in vulputate velit esse molestie consequat, vel illum dolore eu feugiat nulla facilisis at vero eros et accumsan et iusto odio dignissim qui blandit praesent luptatum zzril delenit augue duis dolore te feugait nulla facilisi.</p>
  <div class="abs" style="left:0;top:200px;width:563px;height:98px;background:var(--blue)"></div>
  <div class="abs" style="left:22px;top:212px;width:1.5px;height:74px;background:#fff"></div>
  <p class="lorem abs" style="left:36px;top:212px;width:510px;color:#fff">Lorem ipsum dolor sit amet, consectetuer adipiscing elit, sed diam nonummy nibh euismod tincidunt ut laoreet dolore magna aliquam erat volutpat. Ut wisi enim ad minim veniam, quis nostrud exerci tation ullamcorper suscipit lobortis nisl ut aliquip ex ea commodo consequat. Duis autem vel eum iriure dolor in hendrerit in vulputate velit esse molestie consequat, vel illum dolore eu feugiat nulla facilisis at vero eros et accumsan et iusto odio dignissim qui blandit praesent luptatum zzril delenit augue duis dolore te feugait nulla facilisi.</p>
  <div class="edge-r" style="background:var(--blue)"></div>
  <div class="slide-no" style="background:var(--blue)">12</div>
</section>

<!-- 13 Map option -->
<section class="slide col-l r7">
  <div class="abs" style="left:0;top:0;width:30px;height:318px;background:var(--slate)"></div>
  <div class="abs" style="left:8px;top:225px;transform:rotate(-90deg);transform-origin:left top;color:#fff;font-size:16px;font-weight:800;white-space:nowrap">MAP OPTION</div>
  <div class="photo" role="img" aria-label="Map of national natural regions and protected parks" style="left:38px;top:13px;width:456px;height:288px;border:1px solid #999;background:linear-gradient(135deg,#bfe3f4,#f3efcf 35%,#e8efc4 60%,#bfe3f4)"></div>
  <div class="brand brand-sm">Terravista NQ</div>
  <div class="slide-no" style="background:var(--slate)">13</div>
</section>

<!-- 14 Add your text -->
<section class="slide col-r r7">
  <div class="photo" role="img" aria-label="Helicopter flying over rugged mountain rock" style="inset:0;background:linear-gradient(135deg,#3f4a52,#7a6550 45%,#2d3238 75%,#a07a52)"></div>
  <div class="abs" style="left:0;top:0;width:243px;height:318px;background:rgba(74,88,102,.88)"></div>
  <div class="abs" style="left:21px;top:18px;color:#fff;font-size:19px;font-weight:700">Add your text here</div>
  <p class="lorem abs" style="left:21px;top:58px;width:210px;color:#eee">Lorem ipsum dolor sit amet, consectetuer adipiscing elit, sed diam nonummy nibh euismod tincidunt ut laoreet dolore magna aliquam erat volutpat. Ut wisi enim ad minim veniam, quis nostrud exerci tation ullamcorper suscipit lobortis nisl ut aliquip</p>
  <p class="lorem abs" style="left:21px;top:178px;width:210px;color:#eee">ex ea commodo consequat. Duis autem vel eum iriure dolor in hendrerit in vulputate velit esse molestie consequat, vel illum dolore eu feugiat nulla facilisis at vero eros et accumsan et iusto odio dignissim qui blandit praesent luptatum zzril delenit augue duis dolore te feugait nulla facilisi.</p>
  <div class="brand" style="right:10px;bottom:12px;font-size:9px;color:#fff">Terravista NQ</div>
</section>

<!-- 15 Bullet points -->
<section class="slide col-l r8">
  <div class="page-title" style="color:var(--slate);font-size:17px;font-weight:600">Bullet point text sample</div>
  <div class="brand brand-sm">Terravista NQ</div>
  <svg class="abs" style="inset:0" width="566" height="318" viewBox="0 0 566 318">
    <g fill="none" stroke-width="1.6" font-family="Montserrat, sans-serif" font-size="28" font-weight="400" text-anchor="middle">
      <circle cx="82" cy="102" r="24" stroke="var(--orange)"/><text x="76" y="112" stroke="var(--orange)" stroke-width="1">1</text>
      <circle cx="82" cy="177" r="24" stroke="var(--green)"/><text x="76" y="187" stroke="var(--green)" stroke-width="1">2</text>
      <circle cx="82" cy="250" r="24" stroke="var(--blue)"/><text x="76" y="260" stroke="var(--blue)" stroke-width="1">3</text>
      <circle cx="336" cy="102" r="24" stroke="var(--slate)"/><text x="330" y="112" stroke="var(--slate)" stroke-width="1">4</text>
      <circle cx="336" cy="177" r="24" stroke="var(--orange)"/><text x="330" y="187" stroke="var(--orange)" stroke-width="1">5</text>
      <circle cx="336" cy="250" r="24" stroke="var(--green)"/><text x="330" y="260" stroke="var(--green)" stroke-width="1">6</text>
    </g>
  </svg>
  <p class="bullet-text" style="left:126px;top:90px">Lorem Ipsum is simply dummy text of the printing and typesetting industry.</p>
  <p class="bullet-text" style="left:126px;top:165px">Lorem Ipsum is simply dummy text of the printing and typesetting industry.</p>
  <p class="bullet-text" style="left:126px;top:238px">Lorem Ipsum is simply dummy text of the printing and typesetting industry.</p>
  <p class="bullet-text" style="left:380px;top:90px">Lorem Ipsum is simply dummy text of the printing and typesetting industry.</p>
  <p class="bullet-text" style="left:380px;top:165px">Lorem Ipsum is simply dummy text of the printing and typesetting industry.</p>
  <p class="bullet-text" style="left:380px;top:238px">Lorem Ipsum is simply dummy text of the printing and typesetting industry.</p>
  <div class="slide-no" style="background:var(--orange)">15</div>
</section>

<!-- 16 Thank you -->
<section class="slide col-r r8">
  <div class="abs" style="left:55px;top:42px;font-size:24px;font-weight:700;color:var(--slate)">THANK YOU</div>
  <div class="abs" style="left:58px;top:80px;width:30px;height:3px;background:var(--slate)"></div>
  <div class="brand" style="right:48px;top:74px;font-size:19px">Terravista NQ</div>
  <div class="photo" role="img" aria-label="Dark textured rock surface" style="left:0;right:0;top:149px;bottom:0;background:linear-gradient(160deg,#333,#1f1f1f 60%,#2a2a2a)"></div>
  <div class="abs" style="right:42px;top:180px;font-size:8px;font-weight:700;color:var(--orange)">PRESENTER NAME</div>
  <svg class="abs" style="left:42px;top:202px" width="16" height="100" viewBox="0 0 16 100"><g fill="none" stroke="#fff" stroke-width="1.3"><path d="M3 2 l4 0 2 4 -2 2 q2 4 5 5 l2 -2 4 2 0 3 q-8 1 -13 -6 q-3 -4 -2 -8z"/><circle cx="8" cy="32" r="6"/><line x1="2" y1="32" x2="14" y2="32"/><ellipse cx="8" cy="32" rx="3" ry="6"/><rect x="1" y="51" width="14" height="9"/><path d="M1 51 l7 5 7 -5"/><path d="M8 88 q-6 -6 -6 -10 a6 6 0 0 1 12 0 q0 4 -6 10z"/><circle cx="8" cy="78" r="2"/></g></svg>
  <div class="abs" style="left:70px;top:205px;font-size:8px;color:#fff;font-weight:500;line-height:24px">(555) 014 2290<br>www.terravistanq.org<br>hello@terravistanq.org<br>Terravista NQ, Suite 410 - 88 Harbour Row, Northgate, NQ A1B 2C3</div>
</section>

</body>
</html>
```